Business Card Design

Quindraw

Industry/Entity Type

Business

Contact Information for Business Card

Harbour Crest Lotto
Harbour Crest Shopping Centre
Kiosk 1 No.47 Marlow Brook way
Marlow Heights
Dale Hoskins
0413528846

```html
<!DOCTYPE html>
<html lang="en">
<head>
<meta charset="utf-8">
<title>Harbour Crest Lotto – Business Card</title>
<link href="https://fonts.googleapis.com/css2?family=Open+Sans:wght@400;600;700&display=swap" rel="stylesheet">
<style>
  :root {
    --brand-blue: #1e73be;
    --partner-blue: #2f47a3;
    --ink: #1a1a1a;
    --card-black: #050505;
    --paper: #ffffff;
    --backdrop: #d9dadc;
  }
  * { box-sizing: border-box; margin: 0; padding: 0; }
  html, body { width: 1200px; height: 900px; overflow: hidden; }
  body {
    background: var(--backdrop);
    font-family: "Open Sans", Arial, sans-serif;
    display: flex;
    flex-direction: column;
    align-items: center;
    justify-content: center;
    gap: 40px;
  }
  .card {
    width: 640px;
    height: 366px;
    position: relative;
    overflow: hidden;
    box-shadow: 0 10px 28px rgba(0,0,0,.25);
  }

  /* Back side */
  .card-back {
    background: var(--brand-blue);
    display: flex;
    align-items: center;
    justify-content: center;
  }
  .card-back .brand-name {
    color: var(--paper);
    font-weight: 700;
    font-size: 40px;
    letter-spacing: 2px;
    text-transform: uppercase;
  }

  /* Front side */
  .card-front { background: var(--paper); }
  .front-top {
    height: 190px;
    position: relative;
  }
  .front-top .brand-name {
    position: absolute;
    right: 36px;
    top: 48px;
    color: var(--brand-blue);
    font-weight: 700;
    font-size: 28px;
    letter-spacing: 1.5px;
    text-transform: uppercase;
  }
  .holder-name {
    position: absolute;
    left: 40px;
    bottom: 22px;
    font-size: 28px;
    font-weight: 400;
    color: var(--ink);
  }
  .holder-name .first { color: var(--brand-blue); }

  .front-bottom {
    position: absolute;
    left: 0; right: 0; bottom: 0;
    height: 176px;
    background: var(--card-black);
  }
  .front-bottom::before {
    content: "";
    position: absolute;
    top: 0;
    left: 74px;
    border-left: 16px solid transparent;
    border-right: 16px solid transparent;
    border-top: 18px solid var(--paper);
  }
  .contact-list {
    list-style: none;
    position: absolute;
    left: 40px;
    top: 26px;
    color: var(--paper);
    font-size: 16px;
    line-height: 1.3;
  }
  .contact-list li {
    display: flex;
    align-items: flex-start;
    gap: 14px;
    margin-bottom: 10px;
  }
  .contact-list svg {
    width: 16px;
    height: 16px;
    flex: none;
    margin-top: 3px;
    fill: var(--paper);
  }
  .partner {
    position: absolute;
    right: 40px;
    top: 62px;
    display: flex;
    align-items: center;
    gap: 10px;
    color: var(--partner-blue);
    font-weight: 700;
    font-size: 30px;
  }
  .partner .dot {
    width: 22px;
    height: 22px;
    border-radius: 50%;
    background: var(--partner-blue);
  }
</style>
</head>
<body>

  <section class="card card-back" aria-label="Card back">
    <div class="brand-name">Harbour Crest Lotto</div>
  </section>

  <section class="card card-front" aria-label="Card front">
    <div class="front-top">
      <div class="brand-name">Harbour Crest Lotto</div>
      <h1 class="holder-name"><span class="first">Dale</span> Hoskins</h1>
    </div>
    <div class="front-bottom">
      <ul class="contact-list">
        <li>
          <svg viewBox="0 0 24 24" aria-hidden="true"><path d="M6.6 10.8a15.1 15.1 0 0 0 6.6 6.6l2.2-2.2c.3-.3.7-.4 1-.2 1.1.4 2.3.6 3.6.6.6 0 1 .4 1 1V20c0 .6-.4 1-1 1C10.6 21 3 13.4 3 4c0-.6.4-1 1-1h3.5c.6 0 1 .4 1 1 0 1.3.2 2.5.6 3.6.1.3 0 .7-.2 1z"/></svg>
          <span>0413528846</span>
        </li>
        <li>
          <svg viewBox="0 0 24 24" aria-hidden="true"><path d="M12 2a7 7 0 0 0-7 7c0 5.2 7 13 7 13s7-7.8 7-13a7 7 0 0 0-7-7zm0 9.5A2.5 2.5 0 1 1 12 6.5a2.5 2.5 0 0 1 0 5z"/></svg>
          <span>Harbour Crest Shopping Centre<br>Kiosk 1 No.47 Marlow Brook way<br>Marlow Heights</span>
        </li>
        <li>
          <svg viewBox="0 0 24 24" aria-hidden="true"><path d="M2 5h20v14H2zm2 2v.5l8 5.5 8-5.5V7zm0 3v7h16v-7l-8 5.5z"/></svg>
          <span>dale.hoskins@harbourmail.com</span>
        </li>
      </ul>
      <div class="partner">
        <span class="dot" aria-hidden="true"></span>
        <span>Quindraw</span>
      </div>
    </div>
  </section>

</body>
</html>
```